Survey App for phone users trying a new phone with Dual connectivity

Survey App Brief<br/>Design For an Android Survey App for users' feedback on Call, SMS, Data and Streaming Experience on their Mobile phones.<br/><br/>Purpose of the App<br/>To ensure that the user's experience is not impacted by the network switching between two network on the special mobile phones they newly started using.<br/><br/>App Requirements:<br/>First screen: The registration screen, where the user needs to enter the following:<br/>Name: text box<br/>Phone Number: text box<br/>Group Number : <br/><br/>An information text:<br/>By Registering I agree to participate in the Survey.<br/><br/>Register: Button<br/><br/>Start Screen - Survey screens (next time user open the App this will be the first screen):<br/>We need feedback for 4 indicators:<br/>Call Experience<br/>SMS Experience<br/>Data Experience<br/>Streaming Experience<br/><br/>Each Experience can be in the form of a questionnaire or Satisfied/ Somewhat Satisfied / Extremely Satisfied form with radio buttons or on a scale of 1 to 5. We need to ensure that the format used is very professional.<br/><br/>An optional text box for the user to enter the comment in a free format.<br/><br/>This can be done in 4 different screens or in one single screen if it does not give a clumsy look.<br/><br/>A Send button at the end to submit the Survey.<br/><br/>We need a burger menu at the top left corner of this screen, which when expanded will provide 5 options:<br/>Edit User Profile<br/>Survey interval Timer<br/>FAQ<br/>Exit<br/>About<br/><br/><br/>Please ensure that the app is simple, friendly, lively and professional at the same time so that it ignites an interest in the user to use the app.<br/>Use Logo as appropriate.
Industry/Entity Type
Telecommunications
Colors
Designer to choose colors to be used in the design.
Look and feel
Each slider illustrates characteristics of the customer's brand and the style your logo design should communicate.

```html
<!DOCTYPE html>
<html lang="en">
<head>
<meta charset="utf-8">
<title>Survey – Call Experience</title>
<link href="https://fonts.googleapis.com/css2?family=Arimo:wght@400;500;600;700&display=swap" rel="stylesheet">
<style>
  :root {
    --bg: #ffffff;
    --ink: #111111;
    --muted: #6b6b6b;
    --ghost: #f3f3f3;
    --accent: #6cc7de;
    --accent-light: #84d8ec;
    --accent-dark: #66c1d9;
    --line: #d6d6d6;
  }
  * { box-sizing: border-box; margin: 0; padding: 0; }
  html, body { width: 1200px; height: 2598px; overflow: hidden; background: var(--bg); }
  body { font-family: "Arimo", Helvetica, Arial, sans-serif; color: var(--ink); position: relative; }

  .status-bar { position: absolute; top: 0; left: 0; width: 1200px; height: 110px; }
  .status-time { position: absolute; left: 40px; top: 40px; font-size: 38px; font-weight: 500; letter-spacing: 1px; }
  .status-icons { position: absolute; right: 40px; top: 44px; }

  .ghost-title { position: absolute; left: -10px; top: 60px; font-size: 318px; font-weight: 500; color: var(--ghost); letter-spacing: 4px; white-space: nowrap; line-height: 1; }
  .screen-title { position: absolute; top: 170px; width: 100%; text-align: center; font-size: 70px; font-weight: 500; letter-spacing: 1px; }

  .survey-card { position: absolute; left: 43px; top: 360px; width: 1114px; height: 1965px; background: var(--bg); border: 4px solid var(--accent); border-top: none; border-radius: 6px; box-shadow: 0 20px 40px rgba(0,0,0,0.18); overflow: hidden; }
  .card-header { position: absolute; left: -4px; top: 0; width: 1114px; height: 424px; background: linear-gradient(180deg, var(--accent-light), var(--accent-dark)); overflow: hidden; box-shadow: 0 14px 24px rgba(0,0,0,0.12); }
  .header-art { position: absolute; left: 740px; top: 60px; width: 400px; height: 380px; background: radial-gradient(circle at 50% 50%, rgba(90,180,210,0.45), rgba(90,180,210,0) 70%); }
  .header-icon { position: absolute; left: 490px; top: 45px; width: 220px; height: 220px; border-radius: 50%; background: radial-gradient(circle, rgba(255,255,255,0.35), rgba(255,255,255,0.05) 70%); }
  .header-ghost { position: absolute; left: 0; top: 250px; font-size: 160px; font-weight: 500; color: rgba(255,255,255,0.15); white-space: nowrap; line-height: 1; }
  .header-title { position: absolute; top: 292px; width: 100%; text-align: center; font-size: 60px; font-weight: 500; color: #fff; }
  .header-cursor { position: absolute; left: 850px; top: 322px; }

  .card-heading { position: absolute; top: 540px; width: 100%; text-align: center; font-size: 57px; font-weight: 500; color: var(--accent); }
  .card-question { position: absolute; top: 652px; width: 100%; text-align: center; font-size: 40px; line-height: 57px; }

  .rating-row { position: absolute; top: 851px; left: 36px; display: flex; gap: 33px; }
  .rating-option { width: 179px; height: 83px; border: 1px solid #e2e2e2; background: #fff; box-shadow: 0 2px 4px rgba(0,0,0,0.12); display: flex; align-items: center; justify-content: center; font-size: 24px; font-weight: 500; }

  .comment-box { position: absolute; left: 40px; top: 1035px; width: 1027px; height: 640px; border: 3px solid var(--line); border-radius: 3px; }
  .comment-placeholder { position: absolute; left: 45px; top: 50px; font-size: 38px; color: var(--muted); letter-spacing: 1px; }

  .submit-button { position: absolute; left: 39px; top: 1739px; width: 1029px; height: 145px; background: var(--accent-dark); border-radius: 8px; box-shadow: 0 14px 26px rgba(0,0,0,0.14); overflow: hidden; }
  .submit-ghost { position: absolute; left: 60px; top: 0; font-size: 200px; font-weight: 600; color: rgba(255,255,255,0.12); white-space: nowrap; line-height: 1; }
  .submit-label { position: absolute; width: 100%; top: 44px; text-align: center; font-size: 54px; font-weight: 600; color: #fff; }
</style>
</head>
<body>
  <div class="status-bar">
    <div class="status-time">9:41</div>
    <svg class="status-icons" width="165" height="34" viewBox="0 0 165 34">
      <rect x="0" y="20" width="7" height="10" rx="1" fill="#111"/>
      <rect x="11" y="15" width="7" height="15" rx="1" fill="#111"/>
      <rect x="22" y="9" width="7" height="21" rx="1" fill="#111"/>
      <rect x="33" y="3" width="7" height="27" rx="1" fill="#111"/>
      <path d="M55 12 a26 26 0 0 1 36 0 l-4 4 a20 20 0 0 0 -28 0z M61 18 a17 17 0 0 1 24 0 l-4 4 a11 11 0 0 0 -16 0z M68 25 a7 7 0 0 1 10 0 l-5 5z" fill="#111"/>
      <rect x="108" y="5" width="50" height="24" rx="6" fill="none" stroke="#111" stroke-width="2"/>
      <rect x="112" y="9" width="42" height="16" rx="3" fill="#111"/>
      <rect x="160" y="13" width="3" height="8" rx="1" fill="#111"/>
    </svg>
  </div>

  <div class="ghost-title" aria-hidden="true">SURVEY</div>
  <h1 class="screen-title">SURVEY</h1>

  <section class="survey-card">
    <div class="card-header">
      <div class="header-art" role="img" aria-label="Faint enlarged support-agent illustration"></div>
      <div class="header-ghost" aria-hidden="true">Call Experi</div>
      <div class="header-icon" role="img" aria-label="Line illustration of a support agent with phone and chat bubble"></div>
      <h2 class="header-title">Call Experience</h2>
      <svg class="header-cursor" width="52" height="58" viewBox="0 0 52 58" aria-hidden="true">
        <path d="M2 2 L50 26 L30 30 L42 52 L34 56 L22 34 L8 46 Z" fill="#fff"/>
      </svg>
    </div>

    <h3 class="card-heading">Please Submit Your Call Experience</h3>
    <p class="card-question">How Would you rate your experience obtaining<br>the renters quote ?</p>

    <div class="rating-row">
      <div class="rating-option">Excellent</div>
      <div class="rating-option">Very Good</div>
      <div class="rating-option">Good</div>
      <div class="rating-option">Fair</div>
      <div class="rating-option">Poor</div>
    </div>

    <div class="comment-box">
      <span class="comment-placeholder">Write your comments here..</span>
    </div>

    <div class="submit-button">
      <div class="submit-ghost" aria-hidden="true">SUBMIT</div>
      <div class="submit-label">SUBMIT</div>
    </div>
  </section>
</body>
</html>
```